Business Card for Yachting Management Company

Need a business card design for a new yachting project management company. Attached is the logo for the company.
Our clients are large yacht owners and captains.
Design must be in the style of the logo. Modern, elegant.

Example of data to show:
Peter Hollis
Project Manager
(+34) 612 738 104
peter@quorvane.net
Quorvane Management - Meridel Tower, Office 22 - KRB - Palma de Mallorca

The data above will have to be changed (by me) for the different people in the company over the next years.

Will be printed using PrintNova (Lustre Card Series). They provide these guidelines for the size:
"the actual size of the card is 1050 x 600 pixels. However, the full bleed size is 1083 x 633 pixels, and the safe printing area is 1008 x 558 pixels."

```html
<!DOCTYPE html>
<html lang="en">
<head>
<meta charset="utf-8">
<title>Quorvane Management – Business Card</title>
<link href="https://fonts.googleapis.com/css2?family=Montserrat:wght@400;500;600;700&display=swap" rel="stylesheet">
<style>
  :root {
    --brand-blue: #1170bb;
    --text-dark: #2a2a2a;
    --swoosh-grey: #8a8a8a;
    --swoosh-grey-light: #d4d4d4;
    --card-white: #ffffff;
    --backdrop: #e9ebee;
  }
  * { margin: 0; padding: 0; box-sizing: border-box; }
  html, body {
    width: 1200px; height: 901px; overflow: hidden;
    background: var(--backdrop);
    font-family: "Montserrat", sans-serif;
  }
  .canvas { position: relative; width: 1200px; height: 901px; }

  .card {
    position: absolute;
    width: 525px; height: 300px;
    background: var(--card-white);
    border-radius: 26px;
    overflow: hidden;
    box-shadow: 0 6px 18px rgba(0,0,0,.12);
  }
  .card--front { left: 70px; top: 130px; }
  .card--back  { left: 605px; top: 470px; }

  .brand-name {
    color: var(--brand-blue);
    font-weight: 600;
    text-transform: uppercase;
    white-space: nowrap;
  }
  .card--front .brand-name {
    position: absolute; left: 0; right: 0; top: 50%;
    transform: translateY(-50%);
    text-align: center;
    font-size: 32px;
    letter-spacing: 2px;
  }

  .card--back .brand-name {
    position: absolute; left: 28px; top: 136px;
    font-size: 17px;
    letter-spacing: 1px;
    line-height: 1.25;
  }

  .divider {
    position: absolute; left: 262px; top: 62px;
    width: 1.5px; height: 132px;
    background: var(--brand-blue);
  }

  .contact {
    position: absolute; left: 278px; top: 58px;
    color: var(--text-dark);
  }
  .contact__name {
    color: var(--brand-blue);
    font-weight: 700;
    font-size: 17px;
    text-transform: uppercase;
    letter-spacing: .3px;
  }
  .contact__role { font-size: 11.5px; margin-top: 1px; }
  .contact__list { list-style: none; margin-top: 9px; font-size: 11px; }
  .contact__list li { display: flex; align-items: center; gap: 6px; line-height: 1.5; }
  .contact__list svg { width: 11px; height: 11px; fill: var(--brand-blue); flex: none; }
  .contact__address { font-size: 10.5px; line-height: 1.4; margin-top: 8px; }

  .swoosh { position: absolute; left: 0; bottom: 0; width: 525px; height: 300px; }
</style>
</head>
<body>
<main class="canvas">

  <section class="card card--front" aria-label="Card front">
    <div class="brand-name">Quorvane Management</div>
  </section>

  <section class="card card--back" aria-label="Card back">
    <svg class="swoosh" viewBox="0 0 525 300" aria-hidden="true">
      <defs>
        <linearGradient id="swooshFill" x1="0" y1="1" x2="1" y2="0">
          <stop offset="0" stop-color="var(--swoosh-grey-light)"/>
          <stop offset="1" stop-color="var(--swoosh-grey)"/>
        </linearGradient>
      </defs>
      <path d="M150 300 Q320 200 525 205 L525 300 Z" fill="url(#swooshFill)"/>
      <path d="M150 300 Q320 200 525 205" fill="none" stroke="var(--brand-blue)" stroke-width="2.5"/>
    </svg>

    <div class="brand-name">Quorvane<br>Management</div>
    <div class="divider"></div>

    <div class="contact">
      <div class="contact__name">Peter Hollis</div>
      <div class="contact__role">Project Manager</div>
      <ul class="contact__list">
        <li>
          <svg viewBox="0 0 24 24"><path d="M6.6 10.8a15.1 15.1 0 0 0 6.6 6.6l2.2-2.2a1 1 0 0 1 1-.25 11.4 11.4 0 0 0 3.6.57 1 1 0 0 1 1 1V20a1 1 0 0 1-1 1A17 17 0 0 1 3 4a1 1 0 0 1 1-1h3.5a1 1 0 0 1 1 1c0 1.25.2 2.45.57 3.57a1 1 0 0 1-.25 1z"/></svg>
          (+34) 612 738 104
        </li>
        <li>
          <svg viewBox="0 0 24 24"><path d="M2 5h20v2l-10 6L2 7z M2 9l10 6 10-6v10H2z"/></svg>
          peter@quorvane.net
        </li>
      </ul>
      <div class="contact__address">
        Quorvane Management - Meridel Tower,<br>
        Office 22 - KRB - Palma de Mallorca
      </div>
    </div>
  </section>

</main>
</body>
</html>
```